Quillmere Financial Plans

I am looking for a complete resdesign of my small financial presentation. This is a Word Doc/PDF that I print off when meeting with people in private. I often present my "two pager" that I have been using for years and years. It tells them the basics of what I do, how I help people and foundational financial principles.

I have recently gone out on my own in business and have completely rebranded. This presentation is my most used tool, so it is the first of many things I would like to redo. I am hoping it will somehow coordinate with the colors of my business, not necessarily the EXACT same 3 colors everywhere, but have the design colors compliment.

I've uploaded all my logo designs, as well as the current "two-pager". I am not against it going to 3 pages if needed. As it will still land on 2 pages with duplex printing.

It has always been VERY simple. I am wanting it built into a more professional and design specific format, to show off my branding, without being over cluttered.

I am completely open to ANY graphics changes. Obviously some are very novice, the house on the last page has always been overly simplified.

```html
<!DOCTYPE html>
<html lang="en">
<head>
<meta charset="utf-8">
<title>Quillmere Financial Plans – Two Pager</title>
<link rel="stylesheet" href="https://fonts.googleapis.com/css2?family=Montserrat:wght@300;400;500;600;700;800&display=swap">
<style>
  :root{
    --green:#22b04b;
    --navy:#0f1e33;
    --grey:#8b9096;
    --panel:#f1f1f2;
    --ink:#2b2f36;
    --maroon:#731515;
    --pill:#bfd8f2;
    --icon:#2c4ea5;
    --white:#ffffff;
    --backdrop:#e4e5e7;
  }
  *{box-sizing:border-box;margin:0;padding:0}
  html,body{width:842px;height:1200px;overflow:hidden;background:var(--backdrop)}
  body{font-family:"Montserrat",sans-serif;color:var(--ink);position:relative}

  .sheet{position:absolute;top:312px;width:842px;height:1200px;transform:scale(.48);transform-origin:0 0;box-shadow:0 6px 24px rgba(0,0,0,.18)}
  .sheet-front{left:12px}
  .sheet-back{left:426px}
  .page{position:relative;width:842px;height:1200px;overflow:hidden;background:var(--white)}
  .abs{position:absolute}

  /* shared */
  .section-bar{left:42px;width:759px;height:42px;background:var(--navy);color:var(--white);font-weight:700;font-size:22px;text-align:center;line-height:42px;letter-spacing:-.2px}
  .section-bar em{font-style:normal;color:var(--green)}
  .brand{text-align:center}
  .brand-name{font-size:46px;letter-spacing:-1px;color:var(--navy);line-height:1}
  .brand-name b{font-weight:800}
  .brand-name span{font-weight:300}
  .brand-sub{margin-top:8px;font-size:15px;font-weight:600;letter-spacing:3px;color:var(--navy);display:flex;justify-content:center;align-items:center;gap:12px}
  .brand-sub::before,.brand-sub::after{content:"";width:38px;height:2px;background:var(--navy)}
  .foot-green{left:0;top:1182px;width:440px;height:18px;background:var(--green);clip-path:polygon(0 0,100% 0,96% 100%,0 100%)}
  .foot-grey{left:430px;top:1182px;width:412px;height:18px;background:var(--grey);clip-path:polygon(4% 0,100% 0,100% 100%,0 100%)}

  /* front page */
  .top-band{left:0;top:0;width:842px;height:180px;background:var(--green)}
  .right-band{right:0;top:0;width:42px;height:232px;background:var(--green)}
  .header-plate{left:0;top:0;width:842px;height:140px}
  .front-brand{left:0;top:36px;width:842px}

  .stat-panel{left:42px;width:759px;background:var(--panel)}
  .stat-tab{left:0;width:207px;height:39px;background:var(--grey);color:var(--white);font-weight:700;font-size:16px;line-height:39px;text-align:right;padding-right:48px;border-radius:0 20px 20px 0}
  .stat-list{left:232px;width:560px;list-style:none;font-size:12.4px;font-weight:400;line-height:17.6px;text-transform:uppercase}
  .stat-list li{position:relative;padding-left:25px}
  .stat-list li::before{content:"";position:absolute;left:2px;top:4px;width:11px;height:11px;border-radius:50%;background:var(--green)}
  .stat-list li::after{content:"";position:absolute;left:5px;top:6px;width:3px;height:5px;border:solid var(--white);border-width:0 1.6px 1.6px 0;transform:rotate(45deg)}
  .stat-list .source{display:block;font-weight:700}

  .service{top:772px;width:130px;text-align:center;font-size:12.5px;font-weight:700;line-height:17px;color:var(--navy);text-transform:uppercase}
  .service-icon{display:block;margin:0 auto 10px;width:54px;height:58px;background:var(--icon);border-radius:6px}
  .amount{left:144px;top:776px;font-size:11px;line-height:14px;font-weight:500;color:var(--navy)}

  .pie-label{font-size:12.5px;fill:var(--white);font-family:"Montserrat",sans-serif}
  .savings-title{left:220px;top:1016px;font-size:15px;font-weight:800;color:var(--navy);line-height:18px}
  .goal-list{left:287px;top:1000px;list-style:none;font-size:10px;font-weight:500;text-transform:uppercase;color:var(--navy)}
  .goal-list li{display:flex;align-items:center;gap:9px;height:27.5px}
  .goal-list li::before{content:"";width:15px;height:15px;border:2px solid var(--maroon)}

  .carrier{width:98px;height:30px;border-radius:10px;background:var(--pill);color:var(--navy);font-size:12.5px;font-weight:600;display:flex;align-items:center;justify-content:center;gap:6px}
  .carrier i{width:8px;height:8px;background:var(--icon);border-radius:50%;display:block}
  .pay-us{left:700px;top:1090px;width:80px;height:32px;background:var(--green);color:var(--white);font-weight:800;font-size:17px;text-align:center;line-height:32px;border-radius:5px}

  /* back page */
  .back-band{left:0;top:0;width:842px;height:52px;background:var(--green)}
  .back-right{right:0;top:0;width:42px;height:230px;background:var(--green)}
  .back-left{left:0;top:0;width:42px;height:70px;background:var(--green)}

  .rate-table{top:105px;width:180px;font-size:14px;font-weight:600;color:var(--navy)}
  .rate-head{display:grid;grid-template-columns:1fr 1fr;height:29px;line-height:29px;background:var(--grey);color:var(--white);font-weight:700;font-size:15px;text-align:center}
  .rate-row{display:grid;grid-template-columns:1fr 1fr;height:34px;line-height:34px;text-align:center}
  .rate-row:nth-child(odd){background:var(--panel)}
  .rate-row .age{color:var(--green);font-weight:700;font-size:13px}
  .rate-row.gap{margin-top:9px}
  .doubles{top:389px;width:180px;height:56px;border:2px solid var(--green);color:var(--navy);font-weight:700;font-size:14px;line-height:17px;text-align:center;display:flex;align-items:center;justify-content:center;text-transform:uppercase}

  .taxes-tag{left:45px;top:519px;width:231px;height:41px;background:var(--navy);color:var(--white);font-weight:800;font-size:27px;line-height:41px;text-align:center}
  .house{left:0;top:500px;width:842px;height:650px}
  .back-brand{left:160px;top:612px;width:530px}

  .tax-col{top:745px;width:158px;display:flex;flex-direction:column;gap:8px}
  .tax-head{height:31px;line-height:31px;background:var(--green);color:var(--white);font-weight:800;font-size:17px;text-align:center}
  .tax-cell{min-height:34px;background:var(--panel);font-size:11.5px;font-weight:500;color:var(--ink);text-transform:uppercase;text-align:center;display:flex;align-items:center;justify-content:center;line-height:13px;padding:4px 6px}
  .tax-cell.tall{min-height:52px}
  .tax-result{top:950px;width:158px;height:33px;border:2px solid var(--grey);color:var(--green);font-weight:800;font-size:13px;line-height:29px;text-align:center}
  .house-label{top:1050px;width:330px;text-align:center;font-size:17px;font-weight:600;color:var(--navy);letter-spacing:.3px}
  .house-rule{left:94px;top:1080px;width:655px;height:2px;background:var(--green)}
  .house-sub{top:1093px;width:330px;text-align:center;font-size:17px;font-weight:700;color:var(--green)}
</style>
</head>
<body>

<!-- FRONT PAGE -->
<div class="sheet sheet-front">
<main class="page">
  <div class="abs top-band"></div>
  <div class="abs right-band"></div>
  <svg class="abs header-plate" viewBox="0 0 842 140" aria-hidden="true">
    <polygon points="222,0 636,0 606,138 250,138" fill="#ffffff"/>
  </svg>
  <header class="abs brand front-brand">
    <div class="brand-name"><b>QUILL</b><span>MERE</span></div>
    <div class="brand-sub">FINANCIAL PLANS</div>
  </header>

  <h1 class="abs section-bar" style="top:138px">THE FINANCIAL <em>CHALLENGE</em></h1>

  <div class="abs stat-panel" style="top:183px;height:180px"></div>
  <div class="abs stat-tab" style="top:258px">SAVINGS</div>
  <ul class="abs stat-list" style="top:198px">
    <li>49% of Canadian employees are living paycheque to paycheque. 25% of Canadians are unable to cover an unexpected $500 expense<span class="source">- National Data Office (Feb 2023)</span></li>
    <li>25% of Canadians need to access their retirement savings early. 20% of Canadians have no savings. 39% of Canadians aged 55-65 less than $5,000 in savings.<span class="source">- Federal Savings Review (June 2023)</span></li>
  </ul>

  <div class="abs stat-tab" style="top:420px">DEBT</div>
  <ul class="abs stat-list" style="top:376px">
    <li>The average Canadian has $22,131 in consumer debt. which excludes mortgages.<span class="source">- Credora Reports (Aug 2024)</span></li>
    <li>Over 55% of Canadians hold credit card debt and the total Canadian household debt has increased to $2.52trillion, including consumer credit, mortgage and non-mortgage loans.<span class="source">- Lenders Council (Aug 2024)</span></li>
  </ul>

  <div class="abs stat-panel" style="top:526px;height:176px"></div>
  <div class="abs stat-tab" style="top:586px">INSURANCE</div>
  <ul class="abs stat-list" style="top:534px">
    <li>45% of Canadians do not have individual life insurance coverage, but 48% say their families would face financial trouble within 6 months of losing someone.<span class="source">-Lifeline Research Intl. (Apr 2023)</span></li>
    <li>2-in-5 Canadians (43% women / 44% men) will be diagosed with a form of cancer or other critical illness during their lifetime. Every 7 seconds.<span class="source">-HealthStat Index (June 2024)</span></li>
  </ul>

  <h2 class="abs section-bar" style="top:720px">WHO ARE WE AND <em>WHAT DO WE DO?</em></h2>

  <div class="abs service" style="left:26px;top:780px"><span class="service-icon" role="img" aria-label="Banknotes icon" style="width:70px;height:40px;margin-top:8px"></span><span style="display:block;margin-top:22px">CASH FLOW</span></div>
  <div class="abs amount">$400/<br>$600</div>
  <svg class="abs" style="left:144px;top:816px" width="32" height="14" viewBox="0 0 32 14" aria-hidden="true"><path d="M1 7H28M22 2L29 7 22 12" stroke="#0f1e33" stroke-width="2" fill="none"/></svg>
  <div class="abs service" style="left:159px"><span class="service-icon" role="img" aria-label="Umbrella icon"></span>CASH FLOW<br>PROTECTION</div>
  <div class="abs service" style="left:288px"><span class="service-icon" role="img" aria-label="Crossed-out credit card icon"></span>DEBT<br>MANAGEMENT</div>
  <div class="abs service" style="left:429px"><span class="service-icon" role="img" aria-label="Ambulance icon" style="width:72px"></span>EMERGENCY<br>FUND</div>
  <div class="abs service" style="left:557px"><span class="service-icon" role="img" aria-label="Piggy bank icon" style="width:62px;border-radius:50%"></span>BUILD<br>WEALTH</div>
  <div class="abs service" style="left:674px"><span class="service-icon" role="img" aria-label="Safe icon" style="width:52px"></span>PRESERVE<br>WEALTH</div>

  <h2 class="abs section-bar" style="top:915px">HOW ARE <em>WE DOING IT?</em></h2>

  <svg class="abs" style="left:40px;top:962px" width="460" height="180" viewBox="0 0 460 180" role="img" aria-label="Pie chart of income split between living expenses, taxes and debt">
    <circle cx="87" cy="87" r="83" fill="#731515"/>
    <path d="M87 4V170M87 82H170" stroke="#ffffff" stroke-width="3"/>
    <text class="pie-label" x="16" y="86">Living</text>
    <text class="pie-label" x="8" y="102">Expenses</text>
    <text class="pie-label" x="108" y="60">Taxes</text>
    <text class="pie-label" x="113" y="132">Debt</text>
    <path d="M166 11H412Q430 11 430 29V154Q430 172 412 172H150" stroke="#22b04b" stroke-width="2.5" fill="none"/>
    <path d="M182 82H228M221 77L229 82 221 87" stroke="#0f1e33" stroke-width="1.8" fill="none"/>
    <path d="M430 88H450M443 82L452 88 443 94" stroke="#22b04b" stroke-width="2.5" fill="none"/>
  </svg>
  <div class="abs savings-title">SAVINGS</div>
  <ul class="abs goal-list">
    <li>Retirement savings</li>
    <li>Children's education</li>
    <li>Proper protection</li>
    <li>Freedom from debt</li>
  </ul>

  <div class="abs carrier" style="left:496px;top:970px"><i></i>Maplewell</div>
  <div class="abs carrier" style="left:598px;top:970px">Harbour Life</div>
  <div class="abs carrier" style="left:700px;top:970px">Solstice Life</div>
  <div class="abs carrier" style="left:496px;top:1013px">Aurelle</div>
  <div class="abs carrier" style="left:598px;top:1013px"><i></i>Pinecrest</div>
  <div class="abs carrier" style="left:700px;top:1013px"><i></i>Ridgeway</div>
  <div class="abs carrier" style="left:496px;top:1056px">Bellwood</div>
  <div class="abs carrier" style="left:598px;top:1056px"><i></i>Summit</div>
  <div class="abs carrier" style="left:496px;top:1099px"><i></i>Unity Mutual</div>
  <div class="abs carrier" style="left:598px;top:1099px">Verano</div>
  <svg class="abs" style="left:733px;top:1054px" width="14" height="32" viewBox="0 0 14 32" aria-hidden="true"><path d="M7 1V29M2 23L7 30 12 23" stroke="#22b04b" stroke-width="2.5" fill="none"/></svg>
  <div class="abs pay-us">PAY US</div>

  <div class="abs foot-green"></div>
  <div class="abs foot-grey"></div>
</main>
</div>

<!-- BACK PAGE -->
<div class="sheet sheet-back">
<main class="page">
  <div class="abs back-band"></div>
  <div class="abs back-right"></div>
  <div class="abs back-left"></div>

  <h2 class="abs section-bar" style="top:42px">RULE OF <em>72</em></h2>

  <div class="abs rate-table" style="left:45px">
    <div class="rate-head"><span>AGE</span><span>4%</span></div>
    <div class="rate-body">
      <div class="rate-row"><span class="age">29</span><span>$10,000</span></div>
      <div class="rate-row"><span class="age">47</span><span>$20,000</span></div>
      <div class="rate-row"><span class="age">65</span><span>$40,000</span></div>
    </div>
  </div>
  <div class="abs rate-table" style="left:235px">
    <div class="rate-head"><span>AGE</span><span>6%</span></div>
    <div class="rate-body">
      <div class="rate-row"><span class="age">29</span><span>$10,000</span></div>
      <div class="rate-row"><span class="age">41</span><span>$20,000</span></div>
      <div class="rate-row"><span class="age">53</span><span>$40,000</span></div>
      <div class="rate-row"><span class="age">65</span><span>$80,000</span></div>
    </div>
  </div>
  <div class="abs rate-table" style="left:426px">
    <div class="rate-head"><span>AGE</span><span>8%</span></div>
    <div class="rate-body">
      <div class="rate-row"><span class="age">29</span><span>$10,000</span></div>
      <div class="rate-row"><span class="age">38</span><span>$20,000</span></div>
      <div class="rate-row"><span class="age">47</span><span>$40,000</span></div>
      <div class="rate-row"><span class="age">56</span><span>$80,000</span></div>
      <div class="rate-row"><span class="age">65</span><span>$160,000</span></div>
    </div>
  </div>
  <div class="abs rate-table" style="left:617px">
    <div class="rate-head"><span>AGE</span><span>12%</span></div>
    <div class="rate-body">
      <div class="rate-row"><span class="age">29</span><span>$10,000</span></div>
      <div class="rate-row"><span class="age">35</span><span>$20,000</span></div>
      <div class="rate-row"><span class="age">41</span><span>$40,000</span></div>
      <div class="rate-row"><span class="age">47</span><span>$80,000</span></div>
      <div class="rate-row"><span class="age">53</span><span>$160,000</span></div>
      <div class="rate-row"><span class="age">59</span><span>$320,000</span></div>
      <div class="rate-row gap"><span class="age">59</span><span>$640,000</span></div>
    </div>
  </div>

  <div class="abs doubles" style="left:45px">Money doubles<br>every 6 years</div>
  <div class="abs doubles" style="left:235px">Money doubles<br>every 9 years</div>
  <div class="abs doubles" style="left:426px">Money doubles<br>every 12 years</div>
  <div class="abs doubles" style="left:617px">Money doubles<br>every 18 years</div>

  <svg class="abs house" viewBox="0 0 842 650" aria-hidden="true">
    <polygon points="12,207 423,16 830,207" fill="none" stroke="#0f1e33" stroke-width="4"/>
    <path d="M56 207V635H787V207" fill="none" stroke="#0f1e33" stroke-width="4"/>
    <path d="M56 518H787" stroke="#0f1e33" stroke-width="4"/>
  </svg>
  <div class="abs taxes-tag">TAXES</div>

  <header class="abs brand back-brand">
    <div class="brand-name"><b>QUILL</b><span>MERE</span></div>
    <div class="brand-sub">FINANCIAL PLANS</div>
  </header>

  <div class="abs tax-col" style="left:92px">
    <div class="tax-head">HOME</div>
    <div class="tax-cell tall">Partner with mortgage brokers for best rates</div>
    <div class="tax-cell tall">Mortgage insurance alternatives</div>
  </div>
  <div class="abs tax-col" style="left:258px">
    <div class="tax-head">RRSP</div>
    <div class="tax-cell">Tax deduction</div>
    <div class="tax-cell">Tax deferred</div>
  </div>
  <div class="abs tax-col" style="left:425px">
    <div class="tax-head">TFSA</div>
    <div class="tax-cell">No tax deductions</div>
    <div class="tax-cell">Tax free growth</div>
    <div class="tax-cell">2009 - $95,000</div>
    <div class="tax-cell">Limit 2023 - $7,000/yr</div>
  </div>
  <div class="abs tax-col" style="left:591px">
    <div class="tax-head">PERM LIFE</div>
    <div class="tax-cell">No tax deduction</div>
    <div class="tax-cell">Qualify</div>
    <div class="tax-cell">Tax deferred growth</div>
    <div class="tax-cell">Tax dedction</div>
  </div>

  <div class="abs tax-result" style="left:92px">SELL</div>
  <div class="abs tax-result" style="left:258px">100% TAX</div>
  <div class="abs tax-result" style="left:425px">100% TAX</div>
  <div class="abs tax-result" style="left:591px">0% TAX</div>

  <div class="abs house-label" style="left:88px">LIFE INSURANCE ILLNESS</div>
  <div class="abs house-label" style="left:422px">DEBT MANAGEMENT</div>
  <div class="abs house-rule"></div>
  <div class="abs house-sub" style="left:88px">CRITICAL/DISABILITY</div>
  <div class="abs house-sub" style="left:422px">CASH FLOW</div>

  <div class="abs foot-green"></div>
  <div class="abs foot-grey"></div>
</main>
</div>

</body>
</html>
```